Invitation - Photos with Santa

We’re doing an event this Christmas for people get photos with Santa.
It’ll be a postcard that we mail to people we know.
Size: 5 x 7, two sided
Details for back of postcard:
Saturday, December 4
10 a.m. - 12 p.m.
18457 Colvin Ln.
Strongsville, OH 44873
The company putting it on is Brightwick. I’ve got a million logo formats so just let me know what you need.
In terms of theme/look/feel for the front of card, I’m a little stuck so I’m open to whatever.
-Skip the line?
-Private Santa party?
-Screw the mall?
Attached is an old one we used last time time we did it.
Let me know if there are any questions!
People I know personally, people with kids, people who private photo with Santa without having to go to the mall

```html
<!DOCTYPE html>
<html lang="en">
<head>
<meta charset="utf-8">
<title>Private Santa Party – Brightwick Postcard</title>
<link rel="stylesheet" href="https://fonts.googleapis.com/css2?family=Libre+Baskerville:wght@400;700&family=Kaushan+Script&display=swap">
<style>
  :root {
    --backdrop: #a9a8a9;
    --card-white: #ffffff;
    --night-deep: #1c0d0a;
    --night-warm: #4a1d12;
    --floor-wood: #3a170d;
    --glow-amber: #c9652a;
    --brand-orange: #f04e23;
    --date-red: #d9341f;
    --ink: #2b2b2b;
    --title-white: #ffffff;
    --suit-red: #a8232a;
    --holly-green: #3f7d48;
    --holly-light: #7fb27a;
    --divider: #555555;
  }
  * { box-sizing: border-box; margin: 0; padding: 0; }
  html, body {
    width: 889px; height: 1200px; overflow: hidden;
    background: var(--backdrop);
  }
  body { position: relative; font-family: "Libre Baskerville", Georgia, serif; }

  .card { position: absolute; left: 110px; width: 669px; height: 477px; overflow: hidden; }
  .card--front { top: 84px; }
  .card--back { top: 639px; background: var(--card-white); }

  /* Front */
  .front-scene {
    position: absolute; inset: 0;
    background: linear-gradient(180deg, var(--night-warm) 0%, #2a120c 30%, var(--night-deep) 62%, var(--floor-wood) 80%, #5a2614 100%);
  }
  .string-lights {
    position: absolute; left: 0; top: 0; width: 669px; height: 120px;
    background: linear-gradient(180deg, rgba(201,101,42,.55) 0%, rgba(201,101,42,0) 100%);
  }
  .santa-photo {
    position: absolute; left: 282px; top: 0; width: 387px; height: 392px;
    background: linear-gradient(90deg, rgba(120,40,30,0) 0%, #6e2a22 18%, #8a8f96 45%, #b7b1ad 62%, var(--suit-red) 100%);
  }
  .headline {
    position: absolute; left: 0; top: 0; width: 360px; height: 360px;
    font-family: "Kaushan Script", cursive; font-weight: 400;
    color: var(--title-white); line-height: 1;
    text-shadow: 3px 3px 0 var(--brand-orange), -3px -3px 0 var(--brand-orange), 3px -3px 0 var(--brand-orange), -3px 3px 0 var(--brand-orange), 0 3px 0 var(--brand-orange), 0 -3px 0 var(--brand-orange);
  }
  .headline__line { position: absolute; white-space: nowrap; }
  .headline__line--private { left: 100px; top: 78px; font-size: 58px; }
  .headline__line--santa { left: 26px; top: 138px; font-size: 92px; }
  .headline__line--party { left: 58px; top: 232px; font-size: 90px; }

  .polaroid {
    position: absolute; background: var(--card-white); padding: 7px 7px 20px;
    width: 120px; height: 126px; box-shadow: 0 3px 6px rgba(0,0,0,.4);
  }
  .polaroid__photo { width: 100%; height: 100%; }
  .polaroid--one { left: 312px; top: 322px; transform: rotate(-4deg); }
  .polaroid--two { left: 420px; top: 334px; transform: rotate(2deg); }
  .polaroid--three { left: 536px; top: 328px; transform: rotate(4deg); }
  .polaroid--one .polaroid__photo { background: linear-gradient(90deg, #2f6f34 0%, #3d7a3a 45%, #b9b2ab 100%); }
  .polaroid--two .polaroid__photo { background: linear-gradient(180deg, #4a1414 0%, #b0282a 55%, #8a2020 100%); }
  .polaroid--three .polaroid__photo { background: linear-gradient(180deg, #6a3a18 0%, #a3262a 55%, #7a1c1c 100%); }

  .brand { position: absolute; display: flex; align-items: center; gap: 8px; color: var(--brand-orange); font-family: "Libre Baskerville", Georgia, serif; font-weight: 700; }
  .brand__mark { display: block; background: var(--brand-orange); }
  .brand--front { left: 70px; top: 404px; font-size: 30px; }
  .brand--front .brand__mark { width: 28px; height: 28px; }

  /* Back */
  .greenery { position: absolute; left: 38px; width: 290px; }
  .greenery--top {
    top: 30px; height: 92px;
    border-radius: 50% 50% 10px 10px / 70% 70% 10px 10px;
    background: linear-gradient(180deg, var(--holly-light) 0%, var(--holly-green) 100%);
  }
  .greenery--bottom {
    top: 384px; height: 78px;
    border-radius: 10px 10px 50% 50% / 10px 10px 70% 70%;
    background: linear-gradient(180deg, var(--holly-green) 0%, var(--holly-light) 100%);
  }
  .event-date { position: absolute; left: 45px; top: 137px; width: 273px; text-align: center; color: var(--date-red); font-size: 23px; line-height: 28px; }
  .event-time {
    position: absolute; left: 45px; top: 169px; width: 273px; height: 29px;
    background: var(--brand-orange); color: var(--card-white);
    text-align: center; font-size: 22px; line-height: 29px;
  }
  .event-pin { position: absolute; left: 172px; top: 212px; }
  .event-address { position: absolute; left: 55px; top: 243px; width: 280px; text-align: center; color: var(--ink); font-size: 23px; line-height: 29px; }
  .brand--back { left: 111px; top: 329px; font-size: 22px; }
  .brand--back .brand__mark { width: 22px; height: 22px; }
  .divider { position: absolute; left: 350px; top: 26px; height: 428px; border-left: 1px dashed var(--divider); }
</style>
</head>
<body>
  <section class="card card--front">
    <div class="front-scene" role="img" aria-label="Dark warm night backdrop with a wooden floor"></div>
    <div class="string-lights" role="img" aria-label="Glowing string lights and falling snow"></div>
    <div class="santa-photo" role="img" aria-label="Photo of a smiling girl taking a selfie on Santa's lap"></div>
    <h1 class="headline">
      <span class="headline__line headline__line--private">Private</span>
      <span class="headline__line headline__line--santa">Santa</span>
      <span class="headline__line headline__line--party">Party?</span>
    </h1>
    <div class="polaroid polaroid--one"><div class="polaroid__photo" role="img" aria-label="Photo of a child in an elf hat whispering to Santa"></div></div>
    <div class="polaroid polaroid--two"><div class="polaroid__photo" role="img" aria-label="Photo of children holding gifts with Santa"></div></div>
    <div class="polaroid polaroid--three"><div class="polaroid__photo" role="img" aria-label="Photo of a group of kids in Santa hats with Santa"></div></div>
    <div class="brand brand--front"><span class="brand__mark"></span><span class="brand__name">Brightwick</span></div>
  </section>

  <section class="card card--back">
    <div class="greenery greenery--top" role="img" aria-label="Watercolor pine branches with gifts, candy canes and berries"></div>
    <p class="event-date">Saturday, December 4</p>
    <p class="event-time">10 a.m. - 12 p.m</p>
    <svg class="event-pin" width="18" height="26" viewBox="0 0 16 24" aria-hidden="true">
      <path d="M8 0C3.6 0 0 3.5 0 7.9 0 13.5 8 24 8 24s8-10.5 8-16.1C16 3.5 12.4 0 8 0z" fill="var(--date-red)"/>
      <circle cx="8" cy="8" r="3.2" fill="#fff"/>
    </svg>
    <p class="event-address">18457 Colvin Ln.<br>Strongsville, OH 44873</p>
    <div class="brand brand--back"><span class="brand__mark"></span><span class="brand__name">Brightwick</span></div>
    <div class="greenery greenery--bottom" role="img" aria-label="Watercolor pine branches with berries and candy"></div>
    <div class="divider"></div>
  </section>
</body>
</html>
```